Real Estate Entrepreneur needs a business card

I am a real estate entrepreneur, I buy houses for investment purposes, I act as a real estate agent representing buyers and sellers in residential home transactions, I am a contractor that does a wide range of home repairs and construction. I'd like a design that can stick with me through the years as my business grows and morphs to fit any niche I decide to pursue as markets change.

Target Market(s)

Anyone with interest that may be related to real estate.

Industry/Entity Type

Real Estate

Contact Information for Business Card

A card that stands out and doesn't put me in any one box. My business will evolve over time and I need a card that can stay relevant.

Colors

Designer to choose colors to be used in the design.

Requirements
Must have
• Character
Nice to have
• I'm open
Should not have
• Cliche houses and hammers

```html
<!DOCTYPE html>
<html lang="en">
<head>
<meta charset="utf-8">
<title>Reed Calder – Business Card</title>
<link href="https://fonts.googleapis.com/css2?family=Montserrat:wght@300;400;600&display=swap" rel="stylesheet">
<style>
  :root {
    --backdrop: #d3d7d7;
    --card-black: #0d0d0d;
    --ink-white: #f2f2f2;
    --ink-silver: #c4c4c4;
    --rule: #8a8a8a;
  }
  * { margin: 0; padding: 0; box-sizing: border-box; }
  html, body {
    width: 1200px; height: 1000px; overflow: hidden;
    background: var(--backdrop);
    font-family: "Montserrat", Arial, sans-serif;
  }
  .card-sheet {
    width: 1200px; height: 1000px;
    display: flex; align-items: center; justify-content: center; gap: 40px;
  }
  .card {
    position: relative;
    width: 540px; height: 309px;
    background: var(--card-black);
    color: var(--ink-white);
    border-radius: 3px;
    box-shadow: 0 10px 24px rgba(0,0,0,0.18);
  }

  /* Front: contact side */
  .card-front .identity {
    position: absolute; right: 318px; top: 114px;
    text-align: right;
  }
  .identity .name {
    font-size: 21px; font-weight: 300; letter-spacing: 2px;
    white-space: nowrap; line-height: 1;
  }
  .identity .role {
    margin-top: 7px; font-size: 10px; font-weight: 400; letter-spacing: 0.3px;
  }
  .card-front .divider {
    position: absolute; left: 232px; top: 140px;
    width: 1px; height: 96px; background: var(--rule);
  }
  .card-front .contact {
    position: absolute; left: 246px; top: 140px;
    list-style: none; font-size: 10.5px; font-weight: 300; line-height: 15px;
  }
  .contact .gap { margin-top: 9px; }
  .contact .site strong { font-weight: 600; }

  /* Back: name side */
  .card-back .wordmark {
    position: absolute; right: 44px; top: 84px;
    color: var(--ink-silver);
    font-weight: 400; font-size: 64px; line-height: 0.98; letter-spacing: 3px;
    text-align: left;
  }
  .wordmark span { display: block; }
</style>
</head>
<body>
  <main class="card-sheet">
    <section class="card card-front" aria-label="Card front with contact details">
      <div class="identity">
        <p class="name">REED CALDER</p>
        <p class="role">Real Estate Agent</p>
      </div>
      <div class="divider"></div>
      <ul class="contact">
        <li>4870 Harbor Street NW</li>
        <li>Westfield AB T3R</li>
        <li class="gap">Telephone 2035550142</li>
        <li>Fax 4035550187</li>
        <li>info@reedcalder.com</li>
        <li class="site">www.<strong>reedcalder</strong>.com</li>
      </ul>
    </section>

    <section class="card card-back" aria-label="Card back with name">
      <h1 class="wordmark"><span>REED</span><span>CALDER</span></h1>
    </section>
  </main>
</body>
</html>
```